Food product label that is 3.5” x 3.5” to fit pint jar.

Modify my design to artistic license. Yellow background, green stripe border not at edge with yellow on outside. Font brush script and papyrus. Cuban and American flags in vertical center, some sort of swordfish between flags. Fish possibly with crown or cartoonized.

```html
<!DOCTYPE html>
<html lang="en">
<head>
<meta charset="utf-8">
<title>Salmarina Jar Label</title>
<link rel="stylesheet" href="https://fonts.googleapis.com/css2?family=Kaushan+Script&family=Macondo&display=swap">
<style>
  :root {
    --label-gold-light: #fbf3b8;
    --label-gold: #f8e497;
    --label-gold-deep: #f4cd6c;
    --border-green: #566d33;
    --ink-brown: #6a3e1e;
    --map-green: #5d7434;
    --art-blue: #6fa6d6;
    --art-red: #c8364a;
  }
  * { margin: 0; padding: 0; box-sizing: border-box; }
  html, body { width: 1200px; height: 1200px; overflow: hidden; background: #ffffff; }
  .label {
    position: relative;
    width: 1200px;
    height: 1200px;
    background: radial-gradient(ellipse at 50% 45%, var(--label-gold-light) 0%, var(--label-gold) 55%, var(--label-gold-deep) 100%);
    color: var(--ink-brown);
    text-align: center;
  }
  .label-frame {
    position: absolute;
    left: 8px; top: 8px; right: 8px; bottom: 8px;
    border: 24px solid var(--border-green);
  }
  .brand-name {
    position: absolute;
    top: 66px; left: 0; right: 0;
    font-family: "Macondo", fantasy;
    font-size: 56px;
    font-weight: 400;
    line-height: 1.2;
    letter-spacing: 1px;
  }
  .product-name {
    position: absolute;
    top: 166px; left: 0; right: 0;
    font-family: "Kaushan Script", cursive;
    font-size: 112px;
    font-weight: 400;
    line-height: 1.1;
  }
  .product-tagline {
    position: absolute;
    top: 300px; left: 0; right: 0;
    font-family: "Kaushan Script", cursive;
    font-size: 34px;
    line-height: 53px;
    font-weight: 400;
  }
  .hero-art {
    position: absolute;
    left: 240px; top: 480px;
    width: 704px; height: 392px;
  }
  .quality-line {
    position: absolute;
    top: 896px; left: 0; right: 0;
    font-family: "Macondo", fantasy;
    font-size: 46px;
    line-height: 1.2;
  }
  .claims-line {
    position: absolute;
    top: 960px; left: 0; right: 0;
    font-family: "Macondo", fantasy;
    font-size: 29px;
    line-height: 1.2;
  }
  .island-map {
    position: absolute;
    left: 460px; top: 1028px;
    width: 276px; height: 96px;
  }
</style>
</head>
<body>
  <main class="label">
    <div class="label-frame"></div>

    <h2 class="brand-name">Marisol Foods</h2>
    <h1 class="product-name">Salmarina</h1>
    <p class="product-tagline">
      A Zesty Savory Authentic Cuban Pickled Marinade<br>
      for Fish. Poultry. and Meats<br>
      An Amazing Appetizer Alone over Crackers!
    </p>

    <svg class="hero-art" viewBox="0 0 704 392" role="img" aria-label="Illustration: crossed Cuban and American flags with a crowned cartoon swordfish leaping between them">
      <defs>
        <linearGradient id="heroTone" x1="0" y1="0" x2="1" y2="0">
          <stop offset="0" stop-color="var(--art-blue)" stop-opacity="0.55"/>
          <stop offset="0.5" stop-color="#cfe3f2" stop-opacity="0.6"/>
          <stop offset="1" stop-color="var(--art-red)" stop-opacity="0.45"/>
        </linearGradient>
      </defs>
      <rect x="0" y="0" width="704" height="392" rx="24" fill="url(#heroTone)"/>
    </svg>

    <p class="quality-line">Finest Premium Quality</p>
    <p class="claims-line">Gluten Free, No Trans Fat, Heart Healthy, Deliciously Addictive</p>

    <svg class="island-map" viewBox="0 0 276 96" role="img" aria-label="Map silhouette of the island of Cuba">
      <rect x="0" y="0" width="276" height="96" rx="40" fill="var(--map-green)" opacity="0.85"/>
    </svg>
  </main>
</body>
</html>
```